Menu revision for Korean Restaurant

I have posted the exact content in a word file that I would like to appear in the menu. Please apply to the template. I will be following up with prices shortly. I am in a hurry and not too picky. Thank you.

Make a menu with revisions.

Page 1: Cover Page
- Replace logo with new uploaded logo

Page 2:
Appetizers
Vegetarian Appetizers

Page 3:
BBQ Items

Page 4:
Signature Dishes

Page 5:
Bokkeum | Stir-Fry

Page 6:
Rice Bowls
Noodles
Hot Soup

Page 7:
Drinks

Target Market(s)

My customers

Industry/Entity Type

Restaurant

Requirements
Must have
• 1. Only use my menu content, template, and font.

```html
<!DOCTYPE html>
<html lang="en">
<head>
<meta charset="utf-8">
<title>Signature Dishes</title>
<link rel="stylesheet" href="https://fonts.googleapis.com/css2?family=Anton&family=Roboto+Condensed:wght@700&family=Lora:wght@400&family=Noto+Sans+KR:wght@400&display=swap">
<style>
  :root {
    --bg: #2c2c2c;
    --gold: #b9a06b;
    --gold-line: #a98f5a;
    --red: #c8282e;
    --text: #e8e6e2;
  }
  html, body { margin: 0; padding: 0; overflow: hidden; }
  body { width: 928px; height: 1200px; background: var(--bg); }
  .menu-page { position: relative; width: 928px; height: 1200px; background: var(--bg); overflow: hidden; }
  .page-frame { position: absolute; inset: 0; }
  .page-title {
    position: absolute; top: 42px; left: 0; width: 100%; margin: 0;
    text-align: center; font-family: "Anton", sans-serif; font-weight: 400;
    font-size: 56px; letter-spacing: 2px; color: var(--red); line-height: 1;
  }
  .dish-column { position: absolute; top: 128px; width: 388px; }
  .dish-column.left { left: 59px; }
  .dish-column.right { left: 478px; }
  .dish {
    margin: 0 0 23px; font-family: "Lora", serif; font-size: 14.6px;
    line-height: 20px; color: var(--text); text-align: justify; hyphens: auto;
  }
  .dish-name { font-family: "Roboto Condensed", sans-serif; font-weight: 700; color: var(--gold); letter-spacing: 0.4px; }
  .dish-korean { font-family: "Noto Sans KR", sans-serif; color: var(--gold); font-size: 13.5px; margin: 0 4px; }
  .section-divider { position: absolute; top: 590px; left: 250px; width: 400px; height: 44px; }
</style>
</head>
<body>
<main class="menu-page">
  <svg class="page-frame" width="928" height="1200" viewBox="0 0 928 1200" aria-hidden="true">
    <g fill="none" stroke="var(--gold-line)" stroke-width="1.4">
      <rect x="31" y="34" width="866" height="1136"/>
      <rect x="46" y="46" width="20" height="20"/>
      <rect x="862" y="46" width="20" height="20"/>
      <rect x="46" y="1139" width="20" height="20"/>
      <rect x="862" y="1139" width="20" height="20"/>
      <rect x="56" y="56" width="20" height="20" fill="var(--bg)"/>
      <rect x="852" y="56" width="20" height="20" fill="var(--bg)"/>
      <rect x="56" y="1129" width="20" height="20" fill="var(--bg)"/>
      <rect x="852" y="1129" width="20" height="20" fill="var(--bg)"/>
    </g>
  </svg>

  <h1 class="page-title">SIGNATURE DISHES</h1>

  <section class="dish-column left">
    <p class="dish"><span class="dish-name">Dwaeji Bossam</span><span class="dish-korean">돼지보쌈</span>Braised pork belly wraps accompanied with a spicy gochu &amp; oyster-puréed radish salad. Served with fresh garlic &amp; jalapeno slices, a side of salty shrimp sauce, and a side of house made ssam-jang soybean paste with choice of boiled Napa cabbage wrap or fresh lettuce wrap</p>
    <p class="dish"><span class="dish-name">Yook-hwe</span><span class="dish-korean">육회</span>Raw sesame steak tartar &amp; egg yolk. Julienned strips of premium beef seasoned and dressed with Korean pear, garlic, &amp; pine nuts</p>
    <p class="dish"><span class="dish-name">Pork Katsu</span><span class="dish-korean">돈까스</span>Pork loin breaded in seasoned panko crust &amp; deep-fried. Dressed with bold katsu sauce and served with radish condiments</p>
    <p class="dish"><span class="dish-name">Chicken Katsu</span><span class="dish-korean">치킨까스</span>Chicken breast breaded in seasoned panko crust &amp; deep-fried. Dressed with bold katsu sauce and served with radish condiments</p>
    <p class="dish"><span class="dish-name">Sweet &amp; Sour Pork</span><span class="dish-korean">탕수육</span>Pork tenderloin fried in a light batter. Served with fresh vegetables and pineapples. Drizzled with house made sweet &amp; sour sauce</p>
  </section>

  <section class="dish-column right">
    <p class="dish"><span class="dish-name">Sweet &amp; Sour Chicken</span><span class="dish-korean">탕수치킨</span>Tender pieces of all white chicken breast fried in a light batter. Served with fresh vegetables and pineapples. Drizzled with house made sweet &amp; sour sauce</p>
    <p class="dish"><span class="dish-name">Sweet &amp; Sour Shrimp</span><span class="dish-korean">탕수새우</span>A generous portion of shrimp fried in a light batter. Served with fresh vegetables and pineapples. Drizzled with house made sweet &amp; sour sauce</p>
    <p class="dish"><span class="dish-name">Bulgogi-in-a-Bowl</span><span class="dish-korean">뚝배기불고기</span>Bulgogi, vermicelli, enoki, button mushrooms, scallions, onions, &amp; carrot garnish all in one bowl &amp; filled to the rim with a hearty bulgogi broth</p>
    <p class="dish"><span class="dish-name">Gobchang Gui</span><span class="dish-korean">곱창구이</span>Sizzling beef chitterlings with tripe and vegetable medley spiced with wild sesame and red pepper oil</p>
    <p class="dish"><span class="dish-name">Chub Mackerel</span><span class="dish-korean">고등어구이</span>Whole bone-in silver belly chub mackerel salted and seared.</p>
  </section>

  <svg class="section-divider" viewBox="0 0 400 44" aria-hidden="false">
    <line x1="5" y1="22" x2="168" y2="22" stroke="var(--gold-line)" stroke-width="1.4"/>
    <line x1="232" y1="22" x2="395" y2="22" stroke="var(--gold-line)" stroke-width="1.4"/>
    <circle cx="200" cy="22" r="21" fill="#8a7650" role="img" aria-label="Round decorative medallion emblem"/>
  </svg>
</main>
</body>
</html>
```